MARINE ENGINE PARTS BIZ SITE NEED TOTAL REDESIGN

Re-design our current site: www.verodakmaritime.com.bd<br/>From the existing site you will have the idea, your creative site to be more attractive, modern and user friendly yet simple. Present version likeness is below 20%. It should be SEO Friendly. Mobile, Tablet and Desktop versions are necessary.<br/>Trust True Fittings, Stay Afloat- is our slogan to be highlighted and placed on a proper location.<br/>CONTACT US ** Form to be created, same section we shall provide pictures of the key contacts once design is approved<br/>CONTACT US ** Communication apps to be designed more professionally, Social media to be added, Testimonials to be added <br/>Target Market(s) / products <br/>Bangladesh for Local biz support and others for International Market, <br/>Product Separating to Local Biz and Intl biz is a good idea <br/>Colors<br/>Designer to stick to our brand colors and theme colors but reduce percentage of usage.<br/>Contents <br/>As it is can be finalized, your suggestions are most welcome, whoever comes with much better contents based on current format will be awarded an additional bonus of USD 150.00 by selecting as 2nd winner (Here we will provide SEO friendly words to rewrite some lines) <br/>Pictures<br/><br/>You may select few pictures from provided gallery and use in suitable places, <br/>Note : these are our own pictures other than designing this site copying is prohibited.<br/><br/>We are available for any discussion <br/><br/>best regards<br/>Oliver <br/><br/><br/><br/><br/>

Target Market(s)

International Shipping Sector

Coding

Coded - Design and coding required

Number of Pages Required

5+ page

Font styles to use
Other font styles liked:
• Any most popular SEO Friendly form, Book Antigua preferred but designer can select others

Colors

Designer to choose colors to be used in the design.

Requirements
Must have
• Environmental friendly these, Go green type
Nice to have
• Max usage of the pictures provided by us
Should not have
• Pictures from other sites, or from Internet

```html
<!DOCTYPE html>
<html lang="en">
<head>
<meta charset="utf-8">
<title>Verodak Maritime BD (Pvt.) Limited</title>
<link href="https://fonts.googleapis.com/css2?family=Libre+Baskerville:wght@400;700&family=Lato:wght@400;700&display=swap" rel="stylesheet">
<style>
:root{
  --maroon:#7a1f45;
  --green:#3a8c52;
  --green-dark:#2c6e3f;
  --ink:#2a2a2a;
  --text:#3a3a3a;
  --light:#f3f3f3;
  --footer:#2b2b2b;
  --white:#ffffff;
  --star:#f5d31a;
}
*{box-sizing:border-box;margin:0;padding:0}
html,body{width:1200px;height:3086px;overflow:hidden}
body{font-family:"Lato",sans-serif;color:var(--text);background:var(--white);position:relative}
.serif{font-family:"Libre Baskerville",serif}
section,header,nav,footer{position:absolute;left:0;width:1200px}
.abs{position:absolute}

/* header */
.site-header{top:0;height:110px}
.brand{left:74px;top:22px;display:flex;align-items:center;gap:12px}
.brand-mark{width:72px;height:72px;background:var(--maroon)}
.brand-name{font-family:"Libre Baskerville",serif;font-size:22px;color:var(--maroon)}
.header-phone{right:74px;top:44px;display:flex;align-items:center;gap:14px;font-family:"Libre Baskerville",serif;font-size:24px;color:var(--ink)}

/* nav */
.main-nav{top:110px;height:52px;background:var(--green)}
.main-nav ul{list-style:none;display:flex;position:absolute;left:110px;top:0;height:52px}
.main-nav li{font-family:"Libre Baskerville",serif;font-size:15px;color:var(--white);line-height:52px;padding:0 18px;margin-right:32px;letter-spacing:.5px}
.main-nav li.active{background:var(--maroon);margin-right:32px}

/* hero */
.hero{top:162px;height:538px;background:linear-gradient(180deg,#9eb3cf 0%,#6f86ad 25%,#3f5688 55%,#2b3b63 80%,#3a3a45 100%)}
.hero-title{top:170px;width:100%;text-align:center;font-family:"Libre Baskerville",serif;font-weight:700;font-size:60px;line-height:64px;color:var(--white);text-shadow:0 2px 6px rgba(0,0,0,.35)}
.btn{display:inline-block;background:var(--green);color:var(--white);font-family:"Libre Baskerville",serif;font-size:16px;border-radius:22px;text-align:center;letter-spacing:.5px}
.hero .btn{position:absolute;left:525px;top:323px;width:151px;height:41px;line-height:41px}
.dots{display:flex;gap:10px;position:absolute}
.dots span{width:10px;height:10px;border-radius:50%;background:var(--white)}
.dots span.on{background:#c0283c}
.hero .dots{left:564px;top:496px}

/* welcome */
.welcome{top:700px;height:551px}
.photo{position:absolute}
.welcome-text{left:615px;top:80px;width:512px}
.welcome-text h1{font-family:"Libre Baskerville",serif;font-weight:400;font-size:31px;line-height:41px;color:var(--ink);letter-spacing:.5px}
.welcome-text p{font-size:14.5px;line-height:27px;margin-top:16px}
.welcome-text h1+p{margin-top:20px}
.welcome-text .btn{margin-top:32px;width:152px;height:42px;line-height:42px}

/* products */
.products{top:1251px;height:543px;background:var(--light)}
.section-title{font-family:"Libre Baskerville",serif;font-weight:400;font-size:31px;color:var(--ink);text-align:center}
.products .section-title{position:absolute;top:56px;width:100%}
.product-card{position:absolute;top:134px;width:331px;text-align:center}
.product-card .thumb{width:331px;height:197px}
.product-card h3{font-family:"Libre Baskerville",serif;font-weight:400;font-size:22px;color:var(--green);margin-top:20px}
.product-card p{font-size:14.5px;line-height:25px;margin-top:6px}
.product-card .more{display:inline-flex;align-items:center;gap:5px;font-family:"Libre Baskerville",serif;font-size:14px;color:var(--maroon);margin-top:14px}
.arrow{position:absolute;top:285px}

/* testimonials */
.testimonials{top:1794px;height:455px;background:linear-gradient(135deg,#2e7a45 0%,#276b3c 40%,#2f7d47 70%,#245f37 100%)}
.testimonials .section-title{position:absolute;top:60px;width:100%;color:var(--white)}
.quote{position:absolute;top:128px;width:512px;text-align:center;color:#e6f0e8}
.stars{display:flex;justify-content:center;gap:4px;margin-bottom:12px}
.quote p{font-size:14.5px;line-height:25px}
.quote h4{font-size:15px;font-weight:700;color:var(--white);margin-top:26px}
.testimonials .dots{left:564px;top:368px}

/* contact */
.contact{top:2249px;height:526px}
.contact h2{position:absolute;left:74px;top:70px;font-family:"Libre Baskerville",serif;font-weight:400;font-size:31px;color:var(--ink)}
.field{position:absolute;height:42px;border:1px solid #cfcfcf;border-radius:21px;font-size:13.5px;color:var(--ink);padding:0 16px;line-height:40px;background:var(--white)}
.field.area{border-radius:10px;line-height:22px;padding-top:10px}
.contact .btn{position:absolute;left:74px;top:403px;width:208px;height:44px;line-height:44px}

/* footer */
.site-footer{top:2775px;height:311px;background:var(--footer);color:#e8e8e8}
.col{position:absolute;top:46px}
.col h5{font-family:"Libre Baskerville",serif;font-weight:400;font-size:20px;color:var(--white);margin-bottom:10px}
.col li{list-style:none;font-size:13px;line-height:32px}
.col .addr{font-size:13px;line-height:25px}
.info-row{display:flex;align-items:center;gap:18px;font-size:13px;line-height:32px}
.social{display:flex;gap:22px;margin-top:22px}
.social span{width:16px;height:16px;border-radius:50%;background:var(--white)}
.copy{font-size:12px;line-height:23px;margin-top:44px}
</style>
</head>
<body>

<header class="site-header">
  <div class="abs brand">
    <div class="brand-mark"></div>
    <span class="brand-name">VERODAK MARITIME BD (PVT.) LIMITED</span>
  </div>
  <div class="abs header-phone">
    <svg width="20" height="20" viewBox="0 0 24 24"><path fill="#7a1f45" d="M6.6 10.8c1.4 2.8 3.8 5.1 6.6 6.6l2.2-2.2c.3-.3.7-.4 1-.2 1.1.4 2.3.6 3.6.6.6 0 1 .4 1 1V20c0 .6-.4 1-1 1C10.6 21 3 13.4 3 4c0-.6.4-1 1-1h3.5c.6 0 1 .4 1 1 0 1.3.2 2.5.6 3.6.1.3 0 .7-.2 1z"/></svg>
    +880 31 552418
  </div>
</header>

<nav class="main-nav">
  <ul>
    <li class="active">HOME</li>
    <li>ABOUT US</li>
    <li>PRODUCTS &amp; STOCKS</li>
    <li>CERTIFICATIONS &amp; QA</li>
    <li>CONTACT US</li>
  </ul>
</nav>

<section class="hero" role="img" aria-label="Harbour at dusk with cargo ships and small boats on the river">
  <h2 class="abs hero-title">Trust True Fittings<br>Stay Afloat</h2>
  <span class="btn">READ MORE</span>
  <div class="dots"><span class="on"></span><span></span><span></span><span></span></div>
</section>

<section class="welcome">
  <div class="photo" role="img" aria-label="Ships moored at a jetty at sunset" style="left:74px;top:59px;width:391px;height:361px;background:linear-gradient(180deg,#5d6f9a 0%,#4a4f70 50%,#a36a4a 80%,#5a3a30 100%)"></div>
  <div class="photo" role="img" aria-label="Close-up of a polished engine piston" style="left:355px;top:125px;width:205px;height:161px;background:linear-gradient(135deg,#6f6f6f,#c9c9c9 45%,#555 100%)"></div>
  <div class="photo" role="img" aria-label="Office desk with laptop and chair" style="left:259px;top:305px;width:301px;height:169px;background:linear-gradient(180deg,#e4e8dc 0%,#cfd6c4 60%,#5a3e2c 100%)"></div>
  <div class="abs welcome-text">
    <h1>Welcome to<br>Verodak Maritime Bd (Pvt.) Limited</h1>
    <p>We believe in Corporate Social Responsibility and by practicing best business ethics, we make sure that all our products and supplies meet green standards, to guarantee that the society we live in is sustainable.</p>
    <p>Over the last decade, many sustainable initiatives are taken within shipping industry worldwide and we are proud to follow this drive. In line with this, we procure new genuine marine parts and reusable parts from credible ship recycling affiliates.</p>
    <span class="btn">READ MORE</span>
  </div>
</section>

<section class="products">
  <h2 class="section-title">Our Products</h2>
  <svg class="arrow" style="left:40px" width="20" height="34" viewBox="0 0 20 34"><path d="M16 3 4 17l12 14" fill="none" stroke="#666" stroke-width="4"/></svg>
  <svg class="arrow" style="left:1140px" width="20" height="34" viewBox="0 0 20 34"><path d="M4 3l12 14L4 31" fill="none" stroke="#666" stroke-width="4"/></svg>

  <article class="product-card" style="left:74px">
    <div class="thumb" role="img" aria-label="Pair of perforated engine filter drums" style="background:linear-gradient(135deg,#3d3d3d,#9a9a9a 50%,#2e2e2e)"></div>
    <h3>Corvane / Stelmar Series</h3>
    <p>Lorem ipsum dolor sit amet, consectetur<br>adipisicing elit, sed do eiusmod.</p>
    <span class="more">Read More <svg width="12" height="12" viewBox="0 0 12 12"><circle cx="6" cy="6" r="6" fill="#7a1f45"/><path d="M5 3l3 3-3 3" fill="none" stroke="#fff" stroke-width="1.6"/></svg></span>
  </article>
  <article class="product-card" style="left:435px">
    <div class="thumb" role="img" aria-label="Red painted engine casing block" style="background:linear-gradient(135deg,#d9d9d9 0%,#b0242b 20%,#8e1b20 80%,#c9c9c9 100%)"></div>
    <h3>HDR, KT Series</h3>
    <p>Lorem ipsum dolor sit amet, consectetur<br>adipisicing elit, sed do eiusmod.</p>
    <span class="more">Read More <svg width="12" height="12" viewBox="0 0 12 12"><circle cx="6" cy="6" r="6" fill="#7a1f45"/><path d="M5 3l3 3-3 3" fill="none" stroke="#fff" stroke-width="1.6"/></svg></span>
  </article>
  <article class="product-card" style="left:796px">
    <div class="thumb" role="img" aria-label="Fuel injection pump assembly on a test bench" style="background:linear-gradient(180deg,#5a5a5a 0%,#c8763d 45%,#b8c8b0 100%)"></div>
    <h3>Tornell Series</h3>
    <p>Lorem ipsum dolor sit amet, consectetur<br>adipisicing elit, sed do eiusmod.</p>
    <span class="more">Read More <svg width="12" height="12" viewBox="0 0 12 12"><circle cx="6" cy="6" r="6" fill="#7a1f45"/><path d="M5 3l3 3-3 3" fill="none" stroke="#fff" stroke-width="1.6"/></svg></span>
  </article>
</section>

<section class="testimonials">
  <h2 class="section-title">Testimonials</h2>
  <div class="quote" style="left:74px">
    <div class="stars">
      <svg width="80" height="13" viewBox="0 0 80 13"><g fill="#f5d31a"><path id="st" d="M6.5 0l1.9 4.2 4.6.4-3.5 3 1.1 4.5-4.1-2.4-4.1 2.4 1.1-4.5-3.5-3 4.6-.4z"/><use href="#st" x="17"/><use href="#st" x="34"/><use href="#st" x="51"/><use href="#st" x="68"/></g></svg>
    </div>
    <p>“ Maecenas vitae tristique orci. Praesent fringilla nibh ante, eget<br>fermentum nibh scelerisque nec. Donec scelerisque blandit euismod luctus lorem vitae justo lacinia, eu lobortis ipsum dignissim. Vivamus at tortor venenatis,&nbsp; finibus odio nec, efficitur purus....”</p>
    <h4>NAME HEADING</h4>
  </div>
  <div class="quote" style="left:613px">
    <div class="stars">
      <svg width="80" height="13" viewBox="0 0 80 13"><g fill="#f5d31a"><use href="#st"/><use href="#st" x="17"/><use href="#st" x="34"/><use href="#st" x="51"/><use href="#st" x="68"/></g></svg>
    </div>
    <p>“ Maecenas vitae tristique orci. Praesent fringilla nibh ante, eget<br>fermentum nibh scelerisque nec. Donec scelerisque blandit euismod luctus lorem vitae justo lacinia, eu lobortis ipsum dignissim. Vivamus at tortor venenatis,&nbsp; finibus odio nec, efficitur purus....”</p>
    <h4>NAME HEADING</h4>
  </div>
  <div class="dots"><span class="on"></span><span></span><span></span><span></span></div>
</section>

<section class="contact">
  <h2>Contact Us</h2>
  <div class="field" style="left:74px;top:141px;width:251px">Name</div>
  <div class="field" style="left:335px;top:141px;width:252px">Email Address</div>
  <div class="field" style="left:74px;top:195px;width:251px">Phone No</div>
  <div class="field" style="left:335px;top:195px;width:252px">Subject
    <svg style="position:absolute;right:22px;top:15px" width="8" height="12" viewBox="0 0 8 12"><path d="M4 0l4 5H0zM4 12 0 7h8z" fill="#333"/></svg>
  </div>
  <div class="field area" style="left:74px;top:248px;width:513px;height:130px">Message</div>
  <span class="btn">SUBMIT</span>
  <div class="photo" role="img" aria-label="Portrait photo of a smiling child holding a tree branch outdoors" style="left:614px;top:76px;width:512px;height:372px;background:linear-gradient(135deg,#5a6b3a 0%,#7d8a52 40%,#a69b6a 65%,#3c4a2a 100%)"></div>
</section>

<footer class="site-footer">
  <div class="col" style="left:74px">
    <h5>Site Map</h5>
    <ul><li>Home</li><li>About Us</li><li>Products &amp; Stocks</li><li>Certifications &amp; Qa</li><li>Contact Us</li></ul>
  </div>
  <div class="col" style="left:343px">
    <h5>Products</h5>
    <ul><li>Aenean scelerisque</li><li>Orci hendrerit</li><li>Ullamcorper sollicitudin</li><li>Vivamus ullamcorper</li><li>Tempus</li></ul>
  </div>
  <div class="col" style="left:615px;width:230px">
    <h5>Contact Info</h5>
    <p class="addr">402, Corvin Tower, Harbour Road<br>P.O Box: 2290, Port Veyra, Coastal District</p>
    <div class="info-row" style="margin-top:4px"><svg width="13" height="13" viewBox="0 0 24 24"><path fill="#fff" d="M6.6 10.8c1.4 2.8 3.8 5.1 6.6 6.6l2.2-2.2c.3-.3.7-.4 1-.2 1.1.4 2.3.6 3.6.6.6 0 1 .4 1 1V20c0 .6-.4 1-1 1C10.6 21 3 13.4 3 4c0-.6.4-1 1-1h3.5c.6 0 1 .4 1 1 0 1.3.2 2.5.6 3.6.1.3 0 .7-.2 1z"/></svg>+971 6 5108 362</div>
    <div class="info-row"><svg width="13" height="11" viewBox="0 0 13 11"><rect width="13" height="11" rx="1" fill="#fff"/><path d="M0 1l6.5 5L13 1" fill="none" stroke="#2b2b2b" stroke-width="1.3"/></svg>info@verodakmaritime.com</div>
    <div class="info-row"><svg width="13" height="13" viewBox="0 0 24 24"><path fill="#fff" d="M12 2C8 2 5 5 5 9c0 5 7 13 7 13s7-8 7-13c0-4-3-7-7-7zm0 9.5A2.5 2.5 0 1 1 12 6.5a2.5 2.5 0 0 1 0 5z"/></svg>Map Direction</div>
  </div>
  <div class="col" style="left:911px">
    <h5 style="font-size:18px">Follow Us</h5>
    <div class="social" aria-label="Social media links"><span></span><span></span><span></span><span></span><span></span></div>
    <p class="copy">Copyright © 2020, Company Name<br>All Right reserved</p>
  </div>
</footer>

</body>
</html>
```